Etiketten-Design für Weinflasche
Sehr gute Zusammenarbeit bei Tag und Nacht, sehr kooperativ ,flexibel und entgegenkommend. Empfehlenswert
Zielgruppe
Weinbau - Eigenbau Wein -Weinverkauf
Aufgabenstellung
Bräuchte oder Suche ein Flaschenetikette für Rotwein der Marke Zweigelt Das Ausmaß der Etikette sollte 8cm Breit und 12cm Hoch sein. Habe meine letzte Etikette beigelegt sie Anhang

```html
<!DOCTYPE html>
<html lang="de">
<head>
<meta charset="utf-8">
<title>Zweigelt 2020 – Flaschenetikett</title>
<link rel="stylesheet" href="https://fonts.googleapis.com/css2?family=Roboto:wght@300;400&family=Roboto+Condensed:wght@400&display=swap">
<style>
  :root {
    --page-bg: #1c2433;
    --label-base: #3c3c3d;
    --label-band: #343435;
    --label-edge: #2c2c2d;
    --pattern-tone-a: #403f40;
    --pattern-tone-b: #4a494a;
    --stripe-blue: rgba(90, 140, 165, 0.45);
    --stripe-light: rgba(200, 215, 225, 0.55);
    --text-light: #cfd2d4;
    --text-muted: #9aa3a8;
    --year-grey: #8e9195;
    --accent-red: #c8201f;
  }
  * { box-sizing: border-box; margin: 0; padding: 0; }
  html, body {
    width: 1005px; height: 1200px; overflow: hidden;
    background: var(--page-bg);
  }
  .canvas { position: relative; width: 1005px; height: 1200px; }
  .wine-label {
    position: absolute; left: 165px; top: 52px;
    width: 674px; height: 1095px;
    background: var(--label-base);
    overflow: hidden;
  }
  .wine-label__edge {
    position: absolute; top: 0; right: 0; width: 38px; height: 100%;
    background: var(--label-edge);
  }
  .band {
    position: absolute; left: 0; width: 100%;
    background: var(--label-band);
  }
  .band--top { top: 0; height: 181px; }
  .band--bottom { bottom: 0; height: 195px; }
  .ornament-field {
    position: absolute; left: 0; top: 181px; width: 100%; height: 719px;
    background: radial-gradient(ellipse at 50% 50%, var(--pattern-tone-b), var(--pattern-tone-a) 75%);
  }
  .stripe { position: absolute; top: 0; height: 100%; }
  .stripe--narrow { left: 123px; width: 95px; background: var(--stripe-blue); }
  .stripe--wide { left: 413px; width: 181px; background: var(--stripe-light); }
  .label-text {
    position: absolute; left: 0; width: 100%; text-align: center;
    font-family: "Roboto", Arial, sans-serif;
  }
  .label-text--estate {
    top: 62px; font-size: 58px; font-weight: 300;
    letter-spacing: 0.32em; color: var(--text-muted);
    padding-left: 0.32em;
  }
  .producer {
    position: absolute; left: 0; top: 395px; width: 100%;
    display: flex; justify-content: center; align-items: center; gap: 18px;
  }
  .producer__mark { width: 34px; height: 34px; background: var(--accent-red); }
  .producer__name {
    font-family: "Roboto Condensed", Arial, sans-serif;
    font-size: 38px; font-weight: 400; color: var(--text-light);
    letter-spacing: 0.04em;
  }
  .label-text--variety {
    top: 580px; font-size: 64px; font-weight: 400;
    letter-spacing: 0.3em; color: var(--text-light);
    padding-left: 0.3em;
  }
  .label-text--vintage {
    top: 920px; font-size: 118px; font-weight: 400;
    color: var(--year-grey); letter-spacing: -0.01em;
  }
</style>
</head>
<body>
  <main class="canvas">
    <section class="wine-label" aria-label="Weinetikett Zweigelt 2020">
      <div class="band band--top"></div>
      <div class="ornament-field" role="img" aria-label="Dezentes Rankenornament mit Weintrauben und Blättern"></div>
      <div class="band band--bottom"></div>
      <div class="wine-label__edge"></div>
      <div class="stripe stripe--narrow"></div>
      <div class="stripe stripe--wide"></div>

      <p class="label-text label-text--estate">WEINBAU</p>
      <div class="producer">
        <span class="producer__mark"></span>
        <span class="producer__name">JOHANNES HOLLERER</span>
      </div>
      <p class="label-text label-text--variety">ZWEIGELT</p>
      <p class="label-text label-text--vintage">2020</p>
    </section>
  </main>
</body>
</html>
```